Letterhead and Business card for Construction company

We need a letterhead and business card with our new company logo. We are based in NY. We develop and build properties.

The design should incorporate some unique feature from the logo (shape, font...). it should look like an extension from it.

Design should be clean and elegant, professional, not too busy.

The letterhead should include:
Logo (attached)
Address
Phone
Email

Please find the attached logo images and AI file.

Target Market(s)

Construction industry professionals

Industry/Entity Type

Construction, Development

Font styles to use
Sans Serif

Colors

Designer to choose colors to be used in the design.

Requirements
Must have
• Design should incorporate logo elements, additional assets are welcome. I'd like to see some other shapes / images invorporated too.

```html
<!DOCTYPE html>
<html lang="en">
<head>
<meta charset="utf-8">
<title>Kestrel Build – Letterhead and Business Card</title>
<link href="https://fonts.googleapis.com/css2?family=Montserrat:wght@400;600;800&family=Michroma&display=swap" rel="stylesheet">
<style>
  :root{
    --orange:#f07c1e;
    --orange-light:#fbd2ac;
    --ink:#111111;
    --grey-text:#8a8a8a;
    --lorem:#c9c9c9;
    --paper:#ffffff;
    --backdrop:#e6e6e6;
    --faint:#e9e9e9;
  }
  *{margin:0;padding:0;box-sizing:border-box}
  html,body{width:1200px;height:1000px;overflow:hidden}
  body{background:var(--backdrop);position:relative;font-family:"Montserrat",sans-serif;color:var(--ink)}

  .letterhead{position:absolute;left:40px;top:85px;width:597px;height:835px;background:var(--paper);overflow:hidden}
  .watermark{position:absolute;font-family:"Montserrat",sans-serif;font-weight:800;color:var(--faint);white-space:nowrap;line-height:1}
  .letterhead .watermark{right:30px;top:125px;font-size:38px}

  .sender{position:absolute;left:77px;top:195px}
  .sender-name{font-size:11px;font-weight:600}
  .sender-title{font-size:8px;color:var(--grey-text);margin-top:4px}
  .letter-date{position:absolute;right:77px;top:195px;font-size:11px;font-style:italic}
  .salutation{position:absolute;left:77px;top:246px;font-size:11px;font-weight:600}
  .letter-body{position:absolute;left:77px;top:274px;width:443px;font-size:10px;line-height:12.1px;color:var(--lorem);text-align:justify}
  .signature-area{position:absolute;left:396px;top:570px;width:40px;height:24px;background:linear-gradient(90deg,#f3f3f3,#e8e8e8);border-radius:3px}
  .signatory{position:absolute;left:398px;top:602px}
  .signatory-name{font-size:11px;font-weight:600}
  .signatory-title{font-size:8px;color:var(--grey-text);margin-top:4px}

  .brand{display:flex;align-items:center;gap:8px;position:absolute}
  .brand-mark{width:14px;height:14px;background:var(--orange)}
  .brand-name{font-weight:800;color:var(--ink);white-space:nowrap;line-height:1}
  .letterhead .brand{left:63px;top:762px}
  .letterhead .brand-name{font-size:26px}

  .contacts{position:absolute;display:grid;grid-template-columns:auto 1px auto;column-gap:9px;row-gap:12px;align-items:center;font-family:"Michroma",sans-serif;font-size:8px;color:var(--orange);text-transform:uppercase}
  .contacts .divider{grid-column:2;grid-row:1 / span 2;width:1px;align-self:stretch;background:var(--orange);opacity:.6}
  .contact{display:flex;align-items:center;gap:5px;white-space:nowrap}
  .contact svg{width:12px;height:12px;flex:none}
  .letterhead .contacts{left:287px;top:769px}

  .card{position:absolute;left:690px;width:424px;height:233px;overflow:hidden}
  .card-front{top:287px;background:var(--paper)}
  .card-back{top:535px;background:linear-gradient(180deg,var(--orange) 0%,var(--orange-light) 45%,var(--orange-light) 60%,var(--orange) 100%)}
  .card-front .brand{left:0;right:0;top:58px;justify-content:center}
  .card-front .brand-name{font-size:24px}
  .card-front .contacts{left:100px;top:152px}
  .card-back .brand{left:0;right:0;top:98px;justify-content:center}
  .card-back .brand-mark{background:var(--ink)}
  .card-back .brand-name{font-size:30px}
  .card-back .web{position:absolute;left:0;right:0;top:174px;text-align:center;font-family:"Michroma",sans-serif;font-size:12px;letter-spacing:2px;color:var(--ink);text-transform:uppercase}
  .card-back .watermark{color:rgba(255,255,255,.18);font-size:34px}
  .card-back .wm-top{right:-40px;top:28px}
  .card-back .wm-bottom{left:-30px;bottom:22px}
</style>
</head>
<body>

<section class="letterhead">
  <div class="watermark" aria-hidden="true">Kestrel Build</div>

  <div class="sender">
    <div class="sender-name">Daniel Marsh</div>
    <div class="sender-title">General Manager</div>
  </div>
  <div class="letter-date">20 Nov 2022</div>

  <p class="salutation">Dear Mr. Kestrel Manager</p>

  <div class="letter-body">
    <p>Lorem ipsum dolor sit amet, consectetuer adipiscing elit, sed diam nonummy nibh euismod tincidunt ut laoreet dolore magna aliquam erat volutpat. Ut wisi enim ad minim veniam, quis nostrud exerci tation ullamcorper suscipit lobortis nisl ut aliquip ex ea commodo consequat. Duis autem vel eum iriure dolor in hendrerit in vulputate velit esse molestie consequat, vel illum dolore eu feugiat nulla facilisis at vero eros et accumsan et iusto odio dignissim qui blandit praesent luptatum zzril delenit augue duis dolore te feugait nulla facilisi.</p>
    <p>Lorem ipsum dolor sit amet, cons ectetuer adipiscing elit, sed diam nonummy nibh euismod tincidunt ut laoreet dolore magna aliquam erat volutpat. Ut wisi enim ad minim veniam, quis nostrud exerci tation ullamcorper suscipit lobortis nisl ut aliquip ex ea commodo consequat.</p>
    <p>Lorem ipsum dolor sit amet, consectetuer adipiscing elit, sed diam nonummy nibh euismod tincidunt ut laoreet dolore magna aliquam erat volutpat. Ut wisi enim ad minim veniam, quis nostrud exerci tation ullamcorper suscipit lobortis nisl ut aliquip ex ea commodo consequat. Duis autem vel eum iriure dolor in hendrerit in vulputate velit esse molestie consequat, vel illum dolore eu feugiat nulla facilisis at vero eros et accumsan et iusto odio dignissim qui blandit praesent luptatum zzril delenit augue duis dolore te</p>
  </div>

  <div class="signature-area" role="img" aria-label="Handwritten signature"></div>
  <div class="signatory">
    <div class="signatory-name">Kestrel General Manager</div>
    <div class="signatory-title">General Manager</div>
  </div>

  <div class="brand">
    <span class="brand-mark"></span>
    <span class="brand-name">Kestrel Build</span>
  </div>

  <div class="contacts">
    <span class="contact">
      <svg viewBox="0 0 12 12"><circle cx="6" cy="6" r="6" fill="var(--orange)"/><rect x="3" y="4" width="6" height="4.2" fill="none" stroke="#fff" stroke-width=".9"/><path d="M3 4 6 6.3 9 4" fill="none" stroke="#fff" stroke-width=".9"/></svg>
      info@kbuild.com
    </span>
    <span class="divider"></span>
    <span class="contact">
      <svg viewBox="0 0 12 12"><circle cx="6" cy="6" r="6" fill="var(--orange)"/><path d="M4 3.2c.5-.3.9-.2 1.1.3l.4.9c.1.3 0 .6-.3.8l-.3.2c.3.7.9 1.3 1.6 1.6l.2-.3c.2-.3.5-.4.8-.3l.9.4c.5.2.6.6.3 1.1-.4.6-1 .9-1.7.7C5.3 8.1 3.9 6.7 3.4 5c-.2-.7.1-1.4.6-1.8z" fill="#fff"/></svg>
      (555) 014-2290
    </span>
    <span class="contact">
      <svg viewBox="0 0 12 12"><circle cx="6" cy="6" r="6" fill="var(--orange)"/><circle cx="6" cy="6" r="3" fill="none" stroke="#fff" stroke-width=".8"/><ellipse cx="6" cy="6" rx="1.3" ry="3" fill="none" stroke="#fff" stroke-width=".8"/><path d="M3 6h6" stroke="#fff" stroke-width=".8"/></svg>
      www.kbuild.com
    </span>
    <span class="contact">
      <svg viewBox="0 0 12 12"><circle cx="6" cy="6" r="6" fill="var(--orange)"/><path d="M6 2.6a2.2 2.2 0 0 0-2.2 2.2C3.8 6.5 6 9.4 6 9.4s2.2-2.9 2.2-4.6A2.2 2.2 0 0 0 6 2.6z" fill="#fff"/><circle cx="6" cy="4.8" r=".8" fill="var(--orange)"/></svg>
      418 Mead Blvd
    </span>
  </div>
</section>

<section class="card card-front">
  <div class="brand">
    <span class="brand-mark"></span>
    <span class="brand-name">Kestrel Build</span>
  </div>
  <div class="contacts">
    <span class="contact">
      <svg viewBox="0 0 12 12"><circle cx="6" cy="6" r="6" fill="var(--orange)"/><rect x="3" y="4" width="6" height="4.2" fill="none" stroke="#fff" stroke-width=".9"/><path d="M3 4 6 6.3 9 4" fill="none" stroke="#fff" stroke-width=".9"/></svg>
      info@kbuild.com
    </span>
    <span class="divider"></span>
    <span class="contact">
      <svg viewBox="0 0 12 12"><circle cx="6" cy="6" r="6" fill="var(--orange)"/><path d="M4 3.2c.5-.3.9-.2 1.1.3l.4.9c.1.3 0 .6-.3.8l-.3.2c.3.7.9 1.3 1.6 1.6l.2-.3c.2-.3.5-.4.8-.3l.9.4c.5.2.6.6.3 1.1-.4.6-1 .9-1.7.7C5.3 8.1 3.9 6.7 3.4 5c-.2-.7.1-1.4.6-1.8z" fill="#fff"/></svg>
      (555) 014-2290
    </span>
    <span class="contact">
      <svg viewBox="0 0 12 12"><circle cx="6" cy="6" r="6" fill="var(--orange)"/><circle cx="6" cy="6" r="3" fill="none" stroke="#fff" stroke-width=".8"/><ellipse cx="6" cy="6" rx="1.3" ry="3" fill="none" stroke="#fff" stroke-width=".8"/><path d="M3 6h6" stroke="#fff" stroke-width=".8"/></svg>
      www.kbuild.com
    </span>
    <span class="contact">
      <svg viewBox="0 0 12 12"><circle cx="6" cy="6" r="6" fill="var(--orange)"/><path d="M6 2.6a2.2 2.2 0 0 0-2.2 2.2C3.8 6.5 6 9.4 6 9.4s2.2-2.9 2.2-4.6A2.2 2.2 0 0 0 6 2.6z" fill="#fff"/><circle cx="6" cy="4.8" r=".8" fill="var(--orange)"/></svg>
      418 Mead Blvd
    </span>
  </div>
</section>

<section class="card card-back">
  <div class="watermark wm-top" aria-hidden="true">Kestrel Build</div>
  <div class="watermark wm-bottom" aria-hidden="true">Kestrel Build</div>
  <div class="brand">
    <span class="brand-mark"></span>
    <span class="brand-name">Kestrel Build</span>
  </div>
  <div class="web">www.kbuild.com</div>
</section>

</body>
</html>
```